Consulting company with focus on aviation needs

We need a new business card design for our company. The company consults with multiple players in the industry like manufacturers and airlines. It is also a supplier and an inter-company level. Given the targeted industry (aviation) it should be both kind of serious, sound, secure, classy, ​​but also a bit technical, innovative. Should not be too playful, however, "fresh", "airy", "ligth" and "suprising" are suitabe attributes. The existing logo shall be used.

Industry/Entity Type

Airlines

```html
<!DOCTYPE html>
<html lang="en">
<head>
<meta charset="utf-8">
<title>Zeranth Business Card</title>
<link rel="stylesheet" href="https://fonts.googleapis.com/css2?family=Questrial&display=swap">
<style>
  :root {
    --backdrop: #dcdad6;
    --card: #f1f2f0;
    --card-edge: #d9dbd8;
    --teal: #13866f;
    --orange: #dd8a26;
    --green: #6aa548;
    --slate: #5b5f63;
    --text: #55585b;
  }
  html, body {
    margin: 0;
    padding: 0;
    width: 1200px;
    height: 1054px;
    overflow: hidden;
    background: var(--backdrop);
    font-family: "Questrial", "Century Gothic", sans-serif;
  }
  .card {
    position: absolute;
    left: 100px;
    top: 224px;
    width: 1000px;
    height: 606px;
    background: var(--card);
    border: 1px solid var(--card-edge);
    box-shadow: 0 10px 30px rgba(0,0,0,0.12);
  }
  .brand-dot {
    position: absolute;
    left: 195px;
    top: 150px;
    width: 164px;
    height: 164px;
    border-radius: 50%;
    background: var(--teal);
  }
  .brand-name,
  .brand-tagline {
    position: absolute;
    left: 27px;
    width: 500px;
    text-align: center;
    white-space: nowrap;
  }
  .brand-name {
    top: 340px;
    font-size: 58px;
    line-height: 62px;
    letter-spacing: 7px;
    color: var(--slate);
  }
  .brand-tagline {
    top: 410px;
    font-size: 20px;
    line-height: 26px;
    color: var(--slate);
  }
  .divider {
    position: absolute;
    left: 536px;
    top: 117px;
    width: 2px;
    height: 395px;
    background: var(--orange);
  }
  .contact > * {
    position: absolute;
    left: 588px;
    margin: 0;
    white-space: nowrap;
    color: var(--text);
  }
  .person-name {
    top: 142px;
    font-size: 39px;
    line-height: 48px;
    font-weight: 400;
    color: var(--teal) !important;
  }
  .person-role {
    top: 194px;
    font-size: 22px;
    line-height: 28px;
  }
  .contact-line {
    display: flex;
    align-items: center;
    font-size: 23px;
    line-height: 38px;
    height: 38px;
  }
  .line-phone { top: 266px; }
  .line-email { top: 303px; }
  .line-web { top: 341px; }
  .contact-icon {
    width: 20px;
    height: 20px;
    margin-right: 16px;
  }
  .highlight { color: var(--teal); }
  .address {
    top: 389px;
    font-size: 23px;
    line-height: 34px;
  }
</style>
</head>
<body>
  <div class="card">
    <span class="brand-dot"></span>
    <div class="brand-name">ZERANTH</div>
    <div class="brand-tagline">Linking Partners - Shaping Solutions</div>

    <div class="divider"></div>

    <div class="contact">
      <h1 class="person-name">John K. Smith</h1>
      <div class="person-role">Managing Director</div>
      <div class="contact-line line-phone">
        <svg class="contact-icon" viewBox="0 0 24 24" aria-hidden="true">
          <path fill="#13866f" d="M3 8c0-3 4-4 9-4s9 1 9 4v2h-5V8H8v2H3z"/>
          <rect x="5" y="11" width="14" height="9" rx="2" fill="#13866f"/>
        </svg>
        +00-112-223-3344
      </div>
      <div class="contact-line line-email">
        <svg class="contact-icon" viewBox="0 0 24 24" aria-hidden="true">
          <rect x="2" y="5" width="20" height="14" fill="#dd8a26"/>
          <path d="M2 5l10 8 10-8" fill="none" stroke="#f1f2f0" stroke-width="1.6"/>
        </svg>
        name@yourwebsite.com
      </div>
      <div class="contact-line line-web">
        <svg class="contact-icon" viewBox="0 0 24 24" aria-hidden="true">
          <circle cx="12" cy="12" r="9" fill="#6aa548"/>
          <path d="M3 12h18M12 3c-4 5-4 13 0 18M12 3c4 5 4 13 0 18" fill="none" stroke="#f1f2f0" stroke-width="1.2"/>
        </svg>
        www.<span class="highlight">yourwebsite</span>.com
      </div>
      <div class="address">123, Street No. 6, City Name<br>Opp. Country 123456</div>
    </div>
  </div>
</body>
</html>
```